Bref créative
Business Card and Stationary for Hosting Company
Velmor
Professional
Tomas Hadley
General Manager
2815 Quillan Brook Road
Building 5 Suite 410
Marietta, GA 30182
tomash@brimtide.net
www.velmorhostingllc.com
Logo on the back
Please use this logo and let me know if you need anything else.

```html
<!DOCTYPE html>
<html lang="en">
<head>
<meta charset="utf-8">
<title>Velmor Stationery</title>
<link href="https://fonts.googleapis.com/css2?family=Open+Sans:wght@400;600;700;800&display=swap" rel="stylesheet">
<style>
  :root{
    --bg:#2a2a2a;
    --orange:#f26a1b;
    --orange-light:#f89a3c;
    --orange-dark:#d9510f;
    --blue:#1f8fd6;
    --blue-light:#4bb3ec;
    --blue-dark:#126bb0;
    --paper:#ffffff;
    --ink:#4a4a4a;
    --muted:#8a8a8a;
    --faint:#e6f2fb;
  }
  *{box-sizing:border-box;margin:0;padding:0}
  html,body{width:1200px;height:961px;overflow:hidden}
  body{background:var(--bg);font-family:"Open Sans",Arial,sans-serif;position:relative;color:var(--ink)}
  .piece{position:absolute;overflow:hidden;box-shadow:0 6px 18px rgba(0,0,0,.45)}

  .brand{display:flex;align-items:center;gap:10px}
  .brand-dot{border-radius:50%;flex:none}
  .brand-name{font-weight:800;letter-spacing:.06em;text-transform:uppercase;line-height:1}
  .tagline{font-size:7px;letter-spacing:.08em;margin-top:4px}

  /* Folder */
  .folder{left:40px;top:40px;width:340px;height:470px;
    background:linear-gradient(150deg,var(--orange-light) 0%,var(--orange) 45%,var(--orange-dark) 100%)}
  .folder .brand{position:absolute;left:50%;top:205px;transform:translateX(-50%)}
  .folder .brand-dot{width:34px;height:34px;background:#fff}
  .folder .brand-name{font-size:38px;color:#fff}
  .folder .tagline{color:#fff;position:absolute;left:0;right:0;top:252px;text-align:center}

  /* Letterhead */
  .letterhead{left:410px;top:40px;width:340px;height:470px;background:var(--paper)}
  .letterhead .brand{position:absolute;left:22px;top:24px;gap:6px}
  .letterhead .brand-dot{width:14px;height:14px;background:var(--orange)}
  .letterhead .brand-name{font-size:17px;color:var(--blue)}
  .letterhead .head-contact{position:absolute;right:22px;top:22px;font-size:6px;line-height:1.6;color:var(--muted)}
  .letterhead .backdrop{position:absolute;left:120px;top:110px;width:210px;height:210px;border-radius:50%;background:var(--faint)}
  .letterhead .waves{position:absolute;left:0;bottom:0;width:100%;height:60px}
  .letterhead .web{position:absolute;right:22px;bottom:28px;font-size:6px;color:var(--muted)}

  /* Envelope */
  .envelope{left:780px;top:40px;width:380px;height:180px;background:var(--paper)}
  .envelope .flap{position:absolute;left:0;top:0;width:100%;height:70px}
  .envelope .brand{position:absolute;left:22px;top:84px;gap:5px}
  .envelope .brand-dot{width:11px;height:11px;background:var(--orange)}
  .envelope .brand-name{font-size:13px;color:var(--blue)}
  .envelope .return{position:absolute;left:22px;top:104px;font-size:6px;line-height:1.6;color:var(--muted)}

  /* Business card front */
  .card{width:350px;height:200px}
  .card-front{left:780px;top:250px;background:var(--paper)}
  .card-front .who{position:absolute;right:22px;top:22px;text-align:right}
  .card-front .name{font-size:17px;font-weight:700;color:var(--blue)}
  .card-front .role{font-size:9px;color:var(--orange);margin-top:2px}
  .card-front .brand{position:absolute;left:22px;top:24px;gap:5px}
  .card-front .brand-dot{width:12px;height:12px;background:var(--orange)}
  .card-front .brand-name{font-size:15px;color:var(--blue)}
  .card-front .details{position:absolute;right:22px;top:76px;text-align:right;font-size:8px;line-height:1.6;color:var(--ink)}
  .card-front .waves{position:absolute;left:0;bottom:0;width:100%;height:36px}

  /* Business card back */
  .card-back{left:780px;top:480px;
    background:linear-gradient(150deg,var(--orange-light),var(--orange) 50%,var(--orange-dark))}
  .card-back .brand{position:absolute;left:50%;top:50%;transform:translate(-50%,-50%)}
  .card-back .brand-dot{width:22px;height:22px;background:#fff}
  .card-back .brand-name{font-size:26px;color:#fff}

  /* Cup wrap */
  .cup{left:40px;top:560px;width:280px;height:360px;
    background:linear-gradient(180deg,var(--blue-light),var(--blue) 55%,var(--blue-dark))}
  .cup .rim{position:absolute;left:0;top:0;width:100%;height:26px;background:#f4f4f4}
  .cup .brand{position:absolute;left:50%;top:170px;transform:translateX(-50%)}
  .cup .brand-dot{width:22px;height:22px;background:#fff}
  .cup .brand-name{font-size:26px;color:#fff}
  .cup .stripe{position:absolute;left:0;bottom:40px;width:100%;height:6px;background:var(--orange)}

  /* Disc */
  .disc{left:380px;top:570px;width:340px;height:340px;border-radius:50%;
    background:radial-gradient(circle at 35% 30%,var(--blue-light),var(--blue) 55%,var(--blue-dark))}
  .disc .hub{position:absolute;left:50%;top:50%;width:110px;height:110px;margin:-55px 0 0 -55px;border-radius:50%;background:#cfd6dc}
  .disc .hole{position:absolute;left:50%;top:50%;width:36px;height:36px;margin:-18px 0 0 -18px;border-radius:50%;background:var(--bg)}
  .disc .brand{position:absolute;left:50%;top:78px;transform:translateX(-50%);gap:6px}
  .disc .brand-dot{width:14px;height:14px;background:#fff}
  .disc .brand-name{font-size:18px;color:#fff}
  .disc .web{position:absolute;left:0;right:0;bottom:60px;text-align:center;font-size:8px;color:#fff}
</style>
</head>
<body>

<section class="piece folder">
  <div class="brand"><span class="brand-dot"></span><span class="brand-name">Velmor</span></div>
  <p class="tagline">Dedicated Hosting | Managed Services | Security</p>
</section>

<section class="piece letterhead">
  <div class="brand"><span class="brand-dot"></span><span class="brand-name">Velmor</span></div>
  <div class="head-contact">
    2815 Quillan Brook Road, Building 5 Suite 410<br>
    Marietta, GA 30182<br>
    Tel 770 555 0142<br>
    Fax 770 555 0143<br>
    tomash@brimtide.net
  </div>
  <div class="backdrop"></div>
  <p class="web">www.velmorhostingllc.com</p>
  <svg class="waves" viewBox="0 0 340 60" preserveAspectRatio="none">
    <path d="M0 38 C90 20 200 52 340 26 L340 60 L0 60Z" fill="var(--orange)"/>
    <path d="M0 46 C110 30 210 58 340 38 L340 60 L0 60Z" fill="var(--blue)"/>
  </svg>
</section>

<section class="piece envelope">
  <svg class="flap" viewBox="0 0 380 70" preserveAspectRatio="none">
    <path d="M0 0 L380 0 L380 8 L190 70 L0 8Z" fill="var(--orange)"/>
  </svg>
  <div class="brand"><span class="brand-dot"></span><span class="brand-name">Velmor</span></div>
  <div class="return">
    2815 Quillan Brook Road<br>
    Building 5 Suite 410<br>
    Marietta, GA 30182
  </div>
</section>

<section class="piece card card-front">
  <div class="brand"><span class="brand-dot"></span><span class="brand-name">Velmor</span></div>
  <div class="who">
    <p class="name">Tomas Hadley</p>
    <p class="role">General Manager</p>
  </div>
  <div class="details">
    2815 Quillan Brook Road<br>
    Building 5 Suite 410<br>
    Marietta, GA 30182<br>
    tomash@brimtide.net<br>
    www.velmorhostingllc.com
  </div>
  <svg class="waves" viewBox="0 0 350 36" preserveAspectRatio="none">
    <path d="M0 18 C100 4 220 30 350 10 L350 36 L0 36Z" fill="var(--orange)"/>
    <path d="M0 26 C120 12 230 36 350 20 L350 36 L0 36Z" fill="var(--blue)"/>
  </svg>
</section>

<section class="piece card card-back">
  <div class="brand"><span class="brand-dot"></span><span class="brand-name">Velmor</span></div>
</section>

<section class="piece cup">
  <div class="rim"></div>
  <div class="brand"><span class="brand-dot"></span><span class="brand-name">Velmor</span></div>
  <div class="stripe"></div>
</section>

<section class="piece disc">
  <div class="brand"><span class="brand-dot"></span><span class="brand-name">Velmor</span></div>
  <div class="hub"></div>
  <div class="hole"></div>
  <p class="web">www.velmorhostingllc.com</p>
</section>

</body>
</html>
```